Velmora Easy to modify Email Template

I need an email template created that can be easily modified for each new email sent. What I'm trying to accomplish is a look and feel that is consistent with each email I send out. In a perfect world, I'd like a template to use as a newsletter/informational with product/service pictures and an easy way to create the text to go with it. Then I'd also like a second email that is for letting my clients know there is a promotion or sale going on. Again, something that can he easily modified. I use mail chimp and MindBody as my platform for emailing. If possible, I'd like a pop-up box or dialog box that will ask the ready to opt-in with their name and email address.
I tried to have this done last year on PixelBazaar but we could never get it to work on Mail Chimp - the black box on the attachment would never display or capture email addresses.
What was created for me last year on PixelBazaar is great with matching colors and different sections. What would be great, if possible, is to create a template where I can add different photos in the same section, different verbiage in the same section, etc.
I hope I explained it well enough.
Updates

Need extra days to review

Target Market(s)

Target market is female - 30 to 65 years old

Industry/Entity Type

Health And Wellness

Font styles to use
Serif
Other font styles liked:
• lato

Requirements
Must have
• 1) must be able to be edited (and not by a designer/programmer)
2) must have an option to capture email addresses so people can opt-in to future email campaigns
3) must have a Zen feel to it. We are a medical spa - a very relaxed office space
4) not be too busy
Nice to have
• I hope this isn't asking too much, but the email needs to be able to run on MailChimp with no glitches. I would like the template(s) to be easily modified. Maybe keep the header and footer the same, back ground the same, and just sections that can be modified. Keep the colors to match my logo and the design from last year.

```html
<!DOCTYPE html>
<html lang="en">
<head>
<meta charset="utf-8">
<title>Velmora MediSpa Newsletter</title>
<link rel="stylesheet" href="https://fonts.googleapis.com/css2?family=Lato:wght@300;400;700;900&family=Open+Sans:wght@600;700&display=swap">
<style>
  :root {
    --green-deep: #1e5c0d;
    --green: #2b6b14;
    --green-band: #2d6a15;
    --ink: #333333;
    --frame: #3a3a3a;
    --paper: #f7f7f5;
    --white: #ffffff;
    --footer: #363636;
  }
  * { margin: 0; padding: 0; box-sizing: border-box; }
  html, body { width: 1200px; height: 3804px; overflow: hidden; }
  body {
    position: relative;
    background: var(--paper);
    font-family: "Lato", sans-serif;
    color: var(--ink);
  }
  .abs { position: absolute; }

  .hero {
    left: 0; top: 0; width: 1200px; height: 820px;
    background: linear-gradient(120deg, #d9d6d2 0%, #eeebe7 40%, #c9c3bc 70%, #e8e4df 100%);
  }
  .hero-wave { left: 0; top: 700px; width: 1200px; height: 180px; }

  .brand-blob { right: 0; top: 0; width: 470px; height: 235px; }
  .brand {
    right: 40px; top: 52px; display: flex; align-items: center; gap: 18px;
    color: var(--white); font-family: "Lato", sans-serif; font-weight: 700;
  }
  .brand-dot { width: 78px; height: 78px; border: 5px solid var(--white); border-radius: 50%; }
  .brand-name { font-size: 62px; line-height: 1; letter-spacing: 1px; }
  .brand-name small { display: block; font-size: 22px; letter-spacing: 8px; text-align: right; margin-top: 4px; }

  .social { left: 0; width: 1200px; top: 852px; display: flex; justify-content: center; gap: 30px; }
  .social span { width: 60px; height: 60px; border-radius: 50%; background: var(--green-deep); display: block; }

  .call {
    left: 354px; top: 932px; width: 492px; height: 62px;
    background: var(--green); border-radius: 12px; color: var(--white);
    font-size: 40px; display: flex; align-items: center; justify-content: center; gap: 14px;
  }
  .call b { font-weight: 700; }

  .offer-frame { left: 64px; top: 1040px; width: 1078px; height: 476px; }
  .quote-mark {
    font-family: "Open Sans", sans-serif; font-weight: 700; font-size: 260px;
    line-height: 1; color: #222;
  }
  .quote-open { left: 22px; top: 970px; }
  .quote-close { left: 1040px; top: 1350px; }
  .offer-text {
    left: 64px; top: 1130px; width: 1078px; text-align: center;
    font-family: "Open Sans", sans-serif; font-weight: 700; color: var(--green-deep);
    font-size: 60px; line-height: 72px; text-transform: uppercase;
  }
  .offer-text .big { font-size: 88px; }

  .intro {
    left: 40px; width: 1120px; text-align: center;
    font-size: 29px; line-height: 44px; font-weight: 300; color: #333;
  }
  .intro .name { color: var(--green); font-weight: 400; }
  .intro-1 { top: 1626px; }
  .intro-2 { top: 1834px; }
  .divider { left: 494px; top: 1770px; width: 200px; height: 6px; background: var(--green-deep); }

  .service {
    width: 454px; height: 296px; border: 6px solid var(--frame); border-radius: 12px; overflow: hidden;
  }
  .service .photo { width: 100%; height: 100%; }
  .service .label {
    position: absolute; bottom: 10px; left: 100px; padding: 4px 18px;
    background: var(--green); color: var(--white); border-radius: 14px;
    font-size: 28px; font-weight: 700; white-space: nowrap;
  }
  .s1 { left: 106px; top: 2058px; }
  .s2 { left: 652px; top: 2058px; }
  .s3 { left: 106px; top: 2408px; }
  .s4 { left: 652px; top: 2408px; }
  .s5 { left: 388px; top: 2760px; width: 446px; height: 290px; }
  .s4 .label { left: 100px; }
  .s5 .label { left: 22px; }

  .newsletter { left: 0; top: 3090px; width: 1200px; height: 364px; background: var(--green-band); }
  .stones {
    left: 40px; top: 3110px; width: 420px; height: 340px; border-radius: 20px;
    background: radial-gradient(ellipse at 40% 60%, #2a2a2a 0%, #3f4a3a 45%, rgba(45,106,21,0) 75%);
  }
  .news-title { left: 580px; top: 3160px; font-size: 44px; color: var(--white); font-weight: 400; }
  .email-field {
    left: 534px; top: 3252px; width: 620px; height: 68px; border: 2px solid var(--white); border-radius: 34px;
    display: flex; align-items: center; justify-content: center; gap: 22px;
    color: var(--white); font-size: 28px; font-weight: 700;
  }
  .subscribe {
    left: 704px; top: 3354px; width: 280px; height: 58px; background: #3d3d3d; border-radius: 29px;
    color: var(--white); font-size: 32px; display: flex; align-items: center; justify-content: center;
  }

  .more {
    left: 364px; top: 3546px; width: 436px; height: 50px; background: var(--green); border-radius: 12px;
    color: var(--white); font-size: 29px; font-weight: 700; display: flex; align-items: center; justify-content: center;
  }
  .site { left: 0; width: 1200px; top: 3596px; text-align: center; font-size: 48px; color: var(--green); font-weight: 400; }

  .footer {
    left: 0; top: 3722px; width: 1200px; height: 82px; background: var(--footer);
    color: var(--white); font-size: 24px; display: flex; align-items: center; justify-content: center;
  }
</style>
</head>
<body>

  <div class="abs hero" role="img" aria-label="Woman relaxing with a clay facial mask applied by brush, head wrapped in a white towel"></div>

  <svg class="abs hero-wave" viewBox="0 0 1200 180" preserveAspectRatio="none" aria-hidden="true">
    <path d="M0 40 C200 120 380 140 560 100 C760 50 900 20 1200 30 L1200 180 L0 180 Z" fill="#f7f7f5"/>
    <path d="M0 40 C200 120 380 140 560 100 C760 50 900 20 1200 30" fill="none" stroke="#2b6b14" stroke-width="4"/>
  </svg>

  <svg class="abs brand-blob" viewBox="0 0 470 235" aria-hidden="true">
    <path d="M60 0 H470 V235 C340 230 200 220 120 170 C40 120 20 50 60 0 Z" fill="#1e5c0d"/>
  </svg>
  <div class="abs brand">
    <span class="brand-dot"></span>
    <span class="brand-name">Velmora<small>MEDISPA</small></span>
  </div>

  <div class="abs social" aria-label="Social links">
    <span></span><span></span><span></span>
  </div>

  <div class="abs call">Call Us: <b>555.410.2275</b></div>

  <svg class="abs offer-frame" viewBox="0 0 1078 476" aria-hidden="true">
    <path d="M100 4 H1074 V356" fill="none" stroke="#3a3a3a" stroke-width="7"/>
    <path d="M4 100 V472 H980" fill="none" stroke="#3a3a3a" stroke-width="7"/>
  </svg>
  <div class="abs quote-mark quote-open">&rdquo;</div>
  <div class="abs quote-mark quote-close">&ldquo;</div>
  <div class="abs offer-text">
    We are offering<br>
    <span class="big">20%</span> off on all services<br>
    and special procedure<br>
    combination deals
  </div>

  <p class="abs intro intro-1"><span class="name">Velmora</span> in Japanese means continual improvement. Our goal is to use a variety of<br>technologies and medical science to help our patients achieve natural beauty.</p>
  <div class="abs divider"></div>
  <p class="abs intro intro-2">Our goals are natural beauty and patient satisfactions. We strive to make sure<br>you are happy with your look. We are committed to enhance your natural beauty.</p>

  <div class="abs service s1">
    <div class="photo" role="img" aria-label="Profile of a woman with red lips holding red rose petals" style="background:linear-gradient(135deg,#3a3a40 0%,#5a4a4a 50%,#8a2a2a 100%)"></div>
    <span class="label">Facial Aesthetic</span>
  </div>
  <div class="abs service s2">
    <div class="photo" role="img" aria-label="Close-up of a freckled woman after laser treatment" style="background:linear-gradient(135deg,#4a5a3a 0%,#b08060 55%,#d8b090 100%)"></div>
    <span class="label">Laser Treatments</span>
  </div>
  <div class="abs service s3">
    <div class="photo" role="img" aria-label="Woman's face showing skin before and after rejuvenation" style="background:linear-gradient(90deg,#d8c6b8 0%,#e8dcd2 50%,#d0d4da 100%)"></div>
    <span class="label">Skin Rejuvenation</span>
  </div>
  <div class="abs service s4">
    <div class="photo" role="img" aria-label="Bottles of skin care products with a blue water splash" style="background:linear-gradient(135deg,#ffffff 0%,#c8d4ee 45%,#2a4aa0 100%)"></div>
    <span class="label">Skin Care Products</span>
  </div>
  <div class="abs service s5">
    <div class="photo" role="img" aria-label="Hands framing a slim waist for body contouring" style="background:linear-gradient(180deg,#c9ccd4 0%,#e2d2c6 50%,#b8bcc8 100%)"></div>
    <span class="label">Body Contouring /Weight Loss</span>
  </div>

  <div class="abs newsletter"></div>
  <div class="abs stones" role="img" aria-label="Stacked black spa stones with a candle, orchid and bamboo leaves"></div>
  <div class="abs news-title">Subscribe to Our Newsletter</div>
  <div class="abs email-field">
    <svg width="40" height="30" viewBox="0 0 40 30" aria-hidden="true">
      <rect x="1" y="1" width="38" height="28" rx="3" fill="#ffffff"/>
      <path d="M2 3 L20 17 L38 3" fill="none" stroke="#2d6a15" stroke-width="3"/>
    </svg>
    Enter Your Email Address
  </div>
  <div class="abs subscribe">SUBSCRIBE</div>

  <div class="abs more">For More Information Visit</div>
  <div class="abs site">www.velmoramedispa.com</div>

  <div class="abs footer">Copyright @ 2019 velmoramedispa</div>

</body>
</html>
```